Business card for Sports Apparel business

DOUBLE SIDED DESIGN
We need business cards for a new sports apparel business. We are developing a protective headband for soccer initially.
Corvell is focused on designing and developing head protection products to reduce the likelihood of concussion when playing sports. Exploring and understanding medical insights, material science research, current and former players experiences and governing bodies guidelines has allowed Corvell to develop the safety, style, form and function requirements of a suitable product to bring to market.
Target Market(s)
Mums buying kits for the sons and daughters. Amateur footballers.
Industry/Entity Type
Sporting Good
Contact Information for Business Card
Martin Ashgrove - CEO
Mobile: +44 7391608254
Email: martin@corvell.co.uk
Tel: 0208 5143927
Helena Pardoe - COO
Mob: +44 7356 409183
Email: helena@corvell.co.uk
Tel: 0208 5143927
Duncan Wyvern - CCO
Mob: +44 7468 230517
Email: duncan@corvell.co.uk
Tel: 0208 5143927
Look and feel

```html
<!DOCTYPE html>
<html lang="en">
<head>
<meta charset="utf-8">
<title>Corvell – Business Card</title>
<link rel="stylesheet" href="https://fonts.googleapis.com/css2?family=Arimo:wght@400;700&display=swap">
<style>
  :root {
    --page-bg: #ececec;
    --card-white: #ffffff;
    --brand-blue: #0a4c92;
    --logo-grey: #3b3b3b;
    --text-white: #ffffff;
  }
  html, body {
    margin: 0;
    padding: 0;
    width: 1200px;
    height: 1116px;
    overflow: hidden;
    background: var(--page-bg);
    font-family: "Arimo", Arial, sans-serif;
  }
  .business-card {
    position: absolute;
    left: 120px;
    top: 258px;
    width: 960px;
    height: 600px;
    background: var(--card-white);
    box-shadow: 0 6px 24px rgba(0, 0, 0, 0.12);
    overflow: hidden;
  }
  .card-band {
    position: absolute;
    inset: 0;
    width: 960px;
    height: 600px;
  }
  .brand-mark {
    position: absolute;
    left: 250px;
    top: 78px;
    display: flex;
    align-items: center;
    gap: 22px;
  }
  .brand-square {
    width: 30px;
    height: 30px;
    background: var(--brand-blue);
  }
  .brand-name {
    font-size: 74px;
    font-weight: 400;
    letter-spacing: 5px;
    color: var(--logo-grey);
    line-height: 1;
  }
  .contact-block {
    position: absolute;
    left: 451px;
    top: 282px;
    color: var(--text-white);
  }
  .person-name {
    font-size: 34px;
    font-weight: 700;
    line-height: 1.15;
    margin: 0;
  }
  .person-role {
    font-size: 32px;
    font-weight: 400;
    line-height: 1.15;
    margin: 0 0 22px 0;
  }
  .contact-list {
    list-style: none;
    margin: 0;
    padding: 0;
  }
  .contact-item {
    display: flex;
    align-items: center;
    gap: 14px;
    font-size: 28px;
    line-height: 1;
    height: 44px;
  }
  .contact-icon {
    width: 28px;
    height: 28px;
    flex: none;
  }
</style>
</head>
<body>
  <div class="business-card">
    <svg class="card-band" viewBox="0 0 960 600" aria-hidden="true">
      <path d="M0 228 H528 L568 178 V228 H960 V600 H0 Z" fill="var(--brand-blue)"/>
    </svg>

    <div class="brand-mark">
      <span class="brand-square"></span>
      <span class="brand-name">CORVELL</span>
    </div>

    <div class="contact-block">
      <p class="person-name">Martin Ashgrove</p>
      <p class="person-role">CEO</p>
      <ul class="contact-list">
        <li class="contact-item">
          <svg class="contact-icon" viewBox="0 0 28 28" aria-label="Mobile">
            <circle cx="14" cy="14" r="14" fill="#fff"/>
            <rect x="9.5" y="6" width="9" height="16" rx="1.5" fill="none" stroke="var(--brand-blue)" stroke-width="1.6"/>
            <circle cx="14" cy="19.3" r="1" fill="var(--brand-blue)"/>
          </svg>
          <span>+44 7391608254</span>
        </li>
        <li class="contact-item">
          <svg class="contact-icon" viewBox="0 0 28 28" aria-label="Email">
            <circle cx="14" cy="14" r="14" fill="#fff"/>
            <rect x="6.5" y="9" width="15" height="10.5" fill="none" stroke="var(--brand-blue)" stroke-width="1.6"/>
            <path d="M6.5 9 L14 15 L21.5 9" fill="none" stroke="var(--brand-blue)" stroke-width="1.6"/>
          </svg>
          <span>martin@corvell.co.uk</span>
        </li>
        <li class="contact-item">
          <svg class="contact-icon" viewBox="0 0 28 28" aria-label="Telephone">
            <circle cx="14" cy="14" r="14" fill="#fff"/>
            <path d="M10 7 L12.5 7 L13.5 11 L11.8 12.3 Q13 15.5 15.7 16.3 L17 14.6 L21 15.6 L21 18 Q20.5 21 17.5 20.7 Q9 19 7.5 10.5 Q7.3 7.5 10 7 Z" fill="var(--brand-blue)"/>
          </svg>
          <span>0208 5143927</span>
        </li>
      </ul>
    </div>
  </div>
</body>
</html>
```